Landing Page For a Free Book

A Landing Page for a Ebook , should had 3 sections , menu in HTML 5
the general idea is to update the current site of [url removed, login to view] without wordpress this design is one of i like [url removed, login to view]

About
Book
and a section similar a portolfio or this one

mostly that is for giving away the ebook

the header should allow zuvrin tracking and pixel for meshwave

for reference
can use this ones

i am willing to accept suggestions and related.

can add a section for social part like meshwave box or comments or related.
i am attaching the book cover.

```html
<!DOCTYPE html>
<html lang="es">
<head>
<meta charset="utf-8">
<title>Free Book Landing Page</title>
<link rel="stylesheet" href="https://fonts.googleapis.com/css2?family=Open+Sans:wght@400;600&family=Oswald:wght@500&display=swap">
<style>
  :root {
    --nav-bg: #353535;
    --nav-text: #ffffff;
    --hero-top: #d9d7cd;
    --hero-pages: #e6dfc8;
    --hero-edge: #9a7450;
    --hero-wood: #7a4328;
    --hero-wood-dark: #5a2e1a;
    --ink: #2e2e2e;
    --light: #ffffff;
  }
  * { margin: 0; padding: 0; box-sizing: border-box; }
  html, body {
    width: 1200px;
    height: 569px;
    overflow: hidden;
    font-family: "Open Sans", Arial, sans-serif;
  }
  .page { position: relative; width: 1200px; height: 569px; }

  .site-nav {
    position: absolute; top: 0; left: 0;
    width: 1200px; height: 83px;
    background: var(--nav-bg);
    display: flex; align-items: center;
    padding-left: 93px;
  }
  .brand { color: var(--nav-text); font-size: 17px; margin-right: 26px; }
  .nav-links { display: flex; list-style: none; gap: 27px; }
  .nav-links a { color: var(--nav-text); text-decoration: none; font-size: 13.5px; }

  .hero {
    position: absolute; top: 83px; left: 0;
    width: 1200px; height: 486px;
  }
  .hero-photo {
    position: absolute; inset: 0;
    background: linear-gradient(180deg,
      var(--hero-top) 0%,
      var(--hero-pages) 22%,
      #d8cfb2 50%,
      var(--hero-edge) 62%,
      var(--hero-wood) 76%,
      var(--hero-wood-dark) 100%);
  }
  .hero-content {
    position: relative;
    display: flex; flex-direction: column; align-items: center;
    text-align: center;
  }
  .social-links {
    display: flex; gap: 18px;
    margin-top: 57px;
    list-style: none;
  }
  .social-links a {
    color: var(--ink); text-decoration: none;
    font-size: 13px; font-weight: 600;
  }
  .company-logo {
    margin-top: 6px;
    font-size: 62px; font-weight: 600;
    color: var(--ink);
    line-height: 1.2;
  }
  .book-title {
    margin-top: 70px;
    font-family: "Oswald", Arial, sans-serif;
    font-weight: 500;
    font-size: 38px;
    color: var(--light);
    line-height: 1.2;
  }
  .download-button {
    margin-top: 14px;
    display: inline-block;
    width: 121px; height: 55px;
    line-height: 52px;
    border: 1px solid var(--light);
    border-radius: 2px;
    font-family: "Oswald", Arial, sans-serif;
    font-weight: 500;
    font-size: 25px;
    color: var(--light);
    text-decoration: none;
  }
</style>
</head>
<body>
<div class="page">
  <nav class="site-nav">
    <span class="brand">Your Company</span>
    <ul class="nav-links">
      <li><a href="#about">Acerca De Nosotros</a></li>
      <li><a href="#portfolio">Portafolio</a></li>
    </ul>
  </nav>

  <header class="hero">
    <div class="hero-photo" role="img" aria-label="Open book lying on a wooden table"></div>
    <div class="hero-content">
      <ul class="social-links">
        <li><a href="#">meshwave</a></li>
        <li><a href="#">chirplane</a></li>
      </ul>
      <h1 class="company-logo">Your Company Logo</h1>
      <h2 class="book-title">Book Name</h2>
      <a class="download-button" href="#book">Dowload!</a>
    </div>
  </header>
</div>
</body>
</html>
```